Webseite für Klempnerei Wendlin GmbH
Zielgruppe
Traditionsreicher Familienbetrieb: Klempnerei für Heizung, Bäder nach Maß und Sanitär, Dachklempnerei, Solar, alternative Energien
Aufgabenstellung
Die Farben der Webseite sollen bitte die gleichen, wie auf der alten Seite sein.
Also blau mit Akzenten in vorwiegend rot und ein wenig gelb.
Insgesamt soll die Webseite klar strukturiert sein, aber dennoch modern wirken.
Die Navigationsleiste bitte in folgender Reihenfolge:
-Start
- Das sind wir
-Leistungsübersicht
- Referenzen
- aktuelle Meldungen
- Kontakt
Die Startseite soll wie folgt gestaltet sein und Call to action wahllos in der Startseite evrteilen:
- großes Headerbild
-Teaser zu' Das sind wir' - Familientradition betonen
- Leistungsübersicht in Boxen mit großem Bild und angedeuteter Verlinkung zu der Leistungsunterseite: Heizung, Bäder nach Maß, Dachklempnerei, Solar, alternative Energien
-Teaser zu Referenzen
- Teaser zu aktuelle Meldungen
- Kontakt mit Map
- Footer mit Aufführung: Mitglied der Innung
-Datenschutz und Impressum
Bei den Inhalten bitte an der alten Webseite orientieren: https://www.heizung-wendlin.example/#
Bilder bitte entsprechende Vorschlagen

```html
<!DOCTYPE html>
<html lang="de">
<head>
<meta charset="utf-8">
<title>Klempnerei Wendlin GmbH – Referenzen &amp; Beiträge</title>
<link rel="stylesheet" href="https://fonts.googleapis.com/css2?family=Questrial&family=Montserrat:wght@700&display=swap">
<style>
  :root {
    --backdrop: #f1f1f1;
    --page: #ffffff;
    --ink: #3a3a3a;
    --brand-blue: #4153a0;
    --band-start: #2f4384;
    --band-end: #1f3b4d;
    --white: #ffffff;
    --photo-worker: #8a93a6;
    --photo-site: #b9ad98;
    --photo-tree-sky: #8fa8c8;
    --photo-tree-leaf: #4f6b2e;
    --photo-solar: #4a5f9a;
  }
  * { box-sizing: border-box; margin: 0; padding: 0; }
  html, body { width: 1200px; height: 1200px; overflow: hidden; background: var(--backdrop); }
  body { position: relative; font-family: "Questrial", sans-serif; color: var(--ink); }

  .page {
    position: absolute; left: 158px; top: 0; width: 884px; height: 1200px;
    background: var(--page); box-shadow: 0 0 8px rgba(0,0,0,0.12); overflow: hidden;
  }
  .abs { position: absolute; }

  .section-title {
    font-weight: 400; font-size: 27px; line-height: 34px; letter-spacing: 3.2px; color: var(--ink);
  }
  .body-copy {
    font-size: 10.3px; line-height: 14.3px; letter-spacing: 0.8px; color: var(--ink);
  }
  .body-copy p + p { margin-top: 14px; }

  /* References */
  .references-title { left: 69px; top: 78px; }
  .references-copy { left: 69px; top: 168px; width: 330px; }
  .photo { position: absolute; }
  .photo-craftsman { left: 442px; top: 43px; width: 270px; height: 344px;
    background: linear-gradient(160deg, #a9b0bc 0%, var(--photo-worker) 45%, #2f3f86 100%); }
  .photo-site { left: 648px; top: 229px; width: 181px; height: 241px;
    background: linear-gradient(180deg, #6a7390 0%, var(--photo-site) 40%, #9c9487 100%); }

  .quote-band { position: absolute; left: 0; height: 35px; background: var(--brand-blue);
    color: var(--white); font-size: 22px; letter-spacing: 3.4px; line-height: 35px;
    padding-left: 68px; box-shadow: 0 2px 4px rgba(0,0,0,0.12); white-space: nowrap; }
  .quote-band--one { top: 389px; width: 339px; }
  .quote-band--two { top: 429px; width: 572px; }

  /* Testimonial */
  .testimonial { left: 0; top: 522px; width: 884px; height: 271px;
    background: linear-gradient(90deg, var(--band-start) 0%, #2b4378 55%, var(--band-end) 100%);
    color: var(--white); text-align: center; }
  .testimonial-stars { position: absolute; left: 0; right: 0; top: 55px; }
  .testimonial-quote { position: absolute; left: 0; right: 0; top: 92px;
    font-size: 18.5px; line-height: 26px; letter-spacing: 2.6px; }
  .testimonial-author { position: absolute; left: 0; right: 0; top: 203px;
    font-size: 11px; letter-spacing: 2.4px; }

  /* News */
  .photo-tree { left: 0; top: 819px; width: 231px; height: 381px;
    background: linear-gradient(160deg, var(--photo-tree-leaf) 0%, #6c8a3c 35%, var(--photo-tree-sky) 65%, #c8d4e4 100%); }
  .photo-solar { left: 642px; top: 915px; width: 242px; height: 285px;
    background: linear-gradient(150deg, #7f8fb8 0%, #53627f 40%, var(--photo-solar) 75%, #2a4fa8 100%); }
  .news-title { left: 231px; width: 411px; top: 898px; text-align: center; }
  .news-copy { left: 231px; width: 411px; top: 988px; text-align: center; }
  .news-button { left: 362px; top: 1094px; width: 151px; height: 36px; background: var(--brand-blue);
    color: var(--white); font-family: "Montserrat", sans-serif; font-weight: 700; font-size: 9.5px;
    letter-spacing: 2.4px; text-align: center; line-height: 36px; text-decoration: none; }
</style>
</head>
<body>
<main class="page">
  <section class="references">
    <h2 class="abs section-title references-title">Unsere Referenzen<br>sprechen für sich.</h2>
    <div class="abs body-copy references-copy">
      <p>Lorem ipsum dolor sit amet, consectetur adipiscing elit. Fusce quis quam non enim blandit tempor. Proin ac tellus accumsan leo sagitti.Lorem ipsum dolor sit amet, consectetur adipiscing elit. Fusce quis quam non enim blandit te</p>
      <p>Lorem ipsum dolor sit amet, consectetur adipiscing elit. Fusce quis quam non enim blandit tempor. Proin ac tellus accumsan leo sagitti.Lorem ipsum dolor sit amet, consectetur adipiscing elit. Fusce quis quam non enim blandit te</p>
    </div>
    <div class="photo photo-craftsman" role="img" aria-label="Foto: lächelnder Handwerker in blauer Latzhose und Kappe mit Klemmbrett"></div>
    <div class="photo photo-site" role="img" aria-label="Foto: Baustelle im Innenraum mit Handwerkern und Werkzeug"></div>
    <div class="quote-band quote-band--one">“Lorem ipsum dolor</div>
    <div class="quote-band quote-band--two">sit amet, condipiscing elit fucas quia.</div>
  </section>

  <section class="abs testimonial" role="img" aria-label="Hintergrundfoto: Installateur bei der Arbeit an Heizungsrohren, blau eingefärbt">
    <svg class="testimonial-stars" width="884" height="20" viewBox="0 0 884 20" aria-hidden="true">
      <g fill="#ffffff">
        <polygon id="star" points="10,0 12.4,7 19.5,7 13.8,11.4 16,18.5 10,14.2 4,18.5 6.2,11.4 0.5,7 7.6,7" transform="translate(391,0)"/>
        <use href="#star" x="25"/><use href="#star" x="50"/><use href="#star" x="75"/><use href="#star" x="100"/>
      </g>
    </svg>
    <blockquote class="testimonial-quote">“Vielen Dank an das ganze Team. Es wurde sich für<br>das Beratungsgespräch Zeit genommen,<br>alles pünktlich und sehr professionell umgesetzt.<br>Es war eine Freude.”</blockquote>
    <p class="testimonial-author">L.Berger</p>
  </section>

  <section class="news">
    <div class="photo photo-tree" role="img" aria-label="Foto: Baumkrone und Hochhaus von unten vor bewölktem Himmel"></div>
    <h2 class="abs section-title news-title">Entdecken Sie unsere<br>aktuellen Beiträge.</h2>
    <p class="abs body-copy news-copy">Lorem ipsum dolor sit amet, consectetur adipiscing elit. Fusce quis quam non enim blandit tempor. Proin ac tellus accumsan leo sagitti.Lorem ipsum dolor sit amet, consectetur adipiscing elit. Fusce quis quam non enim blandit te</p>
    <a class="abs news-button" href="#">Zu den News.</a>
    <div class="photo photo-solar" role="img" aria-label="Foto: Handwerker im karierten Hemd legt die Hand auf eine Solaranlage"></div>
  </section>
</main>
</body>
</html>
```